New Business Card Design Project

Want a simple but attention grabbing business card. Back Side having mainly our logo and basic info-the front side a typical business card.

Contact Information for Business Card

Hearth & Basin Works
218 NW Larkfield Rd. Suite 207
Ankeny, Iowa 50021

phone- 515.284.7093

website is -hbwplains.com

```html
<!DOCTYPE html>
<html lang="en">
<head>
<meta charset="UTF-8">
<title>Hearth &amp; Basin Works – Business Card</title>
<link href="https://fonts.googleapis.com/css2?family=Open+Sans:wght@400;700;800&display=swap" rel="stylesheet">
<style>
  :root {
    --backdrop: #1b1d21;
    --card-white: #ffffff;
    --card-navy: #0b1729;
    --brand-orange: #ef5a24;
    --brand-blue: #2f7cc6;
    --muted-blue: #3f6f9f;
    --text-grey: #4a4a4a;
  }
  * { margin: 0; padding: 0; box-sizing: border-box; }
  html, body {
    width: 1200px; height: 900px; overflow: hidden;
    background: var(--backdrop);
    font-family: "Open Sans", Arial, sans-serif;
  }
  .canvas {
    width: 1200px; height: 900px;
    display: flex; flex-direction: column;
    align-items: center; justify-content: center; gap: 36px;
  }
  .card {
    width: 700px; height: 400px;
    box-shadow: 0 14px 30px rgba(0,0,0,.5);
    position: relative;
  }
  /* Front */
  .card-front {
    background: var(--card-white);
    display: flex; align-items: center;
  }
  .brand-block {
    width: 330px; padding-left: 44px;
    display: flex; align-items: center; gap: 12px;
  }
  .brand-mark {
    width: 18px; height: 18px; flex: none;
    background: var(--brand-blue);
  }
  .brand-name {
    color: var(--brand-orange);
    font-weight: 800; font-size: 27px; line-height: 1.15;
    text-transform: uppercase; letter-spacing: .5px;
  }
  .divider {
    width: 2px; height: 200px; background: var(--brand-orange);
  }
  .contact-block {
    padding-left: 34px; color: var(--text-grey);
    font-size: 17px; line-height: 1.45;
  }
  .person-name {
    color: var(--brand-orange); font-weight: 800;
    font-size: 24px; text-transform: uppercase; letter-spacing: .5px;
    line-height: 1.2;
  }
  .person-title { margin-bottom: 10px; }
  .address { margin-bottom: 8px; }
  .contact-line { display: flex; align-items: center; gap: 8px; }
  .contact-line svg { width: 15px; height: 15px; flex: none; fill: var(--brand-blue); }
  /* Back */
  .card-back {
    background: var(--card-navy);
    display: flex; align-items: center; justify-content: center;
  }
  .back-name {
    color: var(--muted-blue);
    font-weight: 800; font-size: 50px; text-transform: uppercase;
    letter-spacing: 1px; text-align: center; line-height: 1.15;
  }
</style>
</head>
<body>
<main class="canvas">
  <section class="card card-front">
    <div class="brand-block">
      <span class="brand-mark"></span>
      <span class="brand-name">Hearth &amp; Basin Works</span>
    </div>
    <div class="divider"></div>
    <div class="contact-block">
      <p class="person-name">Dale Verhoef</p>
      <p class="person-title">President</p>
      <p class="address">218 NW Larkfield Rd. Suite 207<br>Ankeny, Iowa 50021</p>
      <p class="contact-line">
        <svg viewBox="0 0 24 24" aria-hidden="true"><path d="M6.6 10.8a15.1 15.1 0 0 0 6.6 6.6l2.2-2.2a1 1 0 0 1 1-.25 11.4 11.4 0 0 0 3.6.57 1 1 0 0 1 1 1V20a1 1 0 0 1-1 1A17 17 0 0 1 3 4a1 1 0 0 1 1-1h3.5a1 1 0 0 1 1 1c0 1.25.2 2.45.57 3.57a1 1 0 0 1-.25 1z"/></svg>
        515.284.7093
      </p>
      <p class="contact-line">
        <svg viewBox="0 0 24 24" aria-hidden="true"><path d="M2 5h20v14H2z" fill="none"/><path d="M2 5h20v2l-10 6L2 7zM2 9l10 6 10-6v10H2z"/></svg>
        info@hbwplains.com
      </p>
      <p class="contact-line">
        <svg viewBox="0 0 24 24" aria-hidden="true"><circle cx="12" cy="12" r="10"/></svg>
        www.hbwplains.com
      </p>
    </div>
  </section>
  <section class="card card-back">
    <p class="back-name">Hearth &amp; Basin<br>Works</p>
  </section>
</main>
</body>
</html>
```